Review Site Redesign

We have a rather ambitious goal to reinvent (redesign) the way bank financial review sites present information. In that respect, we’re looking for an innovative creative design.
As examples of what I would call bad or boring design please look at the following sites:
1. http://brisklend.example/se
2. http://vantorquay.example/se/privatlan
3. http://glimsworth.example/no
These are the traditional way these types of review sites are organized: dull and boring. I think we can do a lot better than that.
I need a site that will capture attention end engage the visitor; a site that will create a more interactive and less passive user experience.
Scope of work should also include logo font and additional content space for articles, FAQ, widgets, social media links, etc.

Not sure what to advise you as best format - maybe a flash or js carousel, gallery, wheel, logo image matrix, or something else.
Maybe some kind of interactive logo matrix such as this site: http://www.quarnibo.example/
Please apply your best creative mind work to this problem.
Also, please think about creative use of background images, stock photos, etc.
For logo font use can use URL “pellrowatt.example” as placeholder.

```html
<!DOCTYPE html>
<html lang="en">
<head>
<meta charset="utf-8">
<title>Pellrowatt – Loan Reviews</title>
<link href="https://fonts.googleapis.com/css2?family=Open+Sans:wght@400;600;700&display=swap" rel="stylesheet">
<style>
:root{
  --page:#dde3ec;
  --navy:#1b2840;
  --navy-2:#22324f;
  --panel-top:#3f5679;
  --panel-bottom:#1e2d48;
  --row-a:#34496c;
  --row-b:#2b3d5d;
  --line:#1a263c;
  --text:#e6ecf5;
  --muted:#b9c5d8;
  --nav:#7d8898;
  --button:#b9bcc2;
  --field:#1b2740;
  --accent:#3d8fe0;
  --star:#e9edf4;
}
*{box-sizing:border-box;margin:0;padding:0}
html,body{width:1200px;height:2341px;overflow:hidden}
body{background:var(--page);font-family:"Open Sans",Arial,sans-serif;color:var(--text);position:relative}
.abs{position:absolute}

/* header */
.socials{left:150px;top:19px;display:flex;gap:9px}
.socials span{width:28px;height:28px;border-radius:4px;background:var(--navy-2);box-shadow:0 2px 3px rgba(0,0,0,.3)}
.brand{left:398px;top:-120px;width:420px;height:238px;border-radius:50%;background:radial-gradient(ellipse at 50% 70%,#3d5479,#1d2b45);border:4px solid #fff;box-shadow:0 3px 8px rgba(0,0,0,.35);display:flex;align-items:flex-end;justify-content:center;padding-bottom:62px}
.brand-name{font-size:35px;font-weight:700;color:#dfe6f0;letter-spacing:1px}
.account{left:897px;top:20px;display:flex;gap:10px}
.btn-dark{background:var(--navy-2);color:#fff;font-size:15px;font-weight:600;padding:8px 13px;border-radius:3px;box-shadow:0 3px 4px rgba(0,0,0,.35)}

.nav{left:168px;top:140px;display:flex;align-items:center;gap:0}
.nav a{color:var(--nav);font-size:16px;text-decoration:none;margin-right:47px;text-transform:uppercase}
.nav a.active{background:var(--navy-2);color:#fff;font-weight:600;padding:10px 20px;border:2px solid #fff;border-radius:3px;box-shadow:0 2px 4px rgba(0,0,0,.3);margin-right:24px}

/* panels */
.panel{background:linear-gradient(180deg,var(--panel-top),var(--panel-bottom));box-shadow:0 10px 12px -6px rgba(0,0,0,.35)}
.lip{height:18px;background:linear-gradient(180deg,#5c7398,#34496c);clip-path:polygon(3% 0,97% 0,100% 100%,0 100%)}

.hero{left:120px;top:200px;width:960px;height:499px}
.hero-copy{left:34px;top:70px;width:290px}
.hero-copy h1{font-size:24px;font-weight:400;margin-bottom:20px}
.hero-copy p{font-size:12px;line-height:21px;color:var(--muted);margin-bottom:20px}
.btn-light{display:inline-block;background:linear-gradient(#d4d7dc,#9da2aa);color:#2a3346;font-size:14px;padding:4px 10px;border-radius:2px;border:1px solid #6b717c}
.hero-art{left:340px;top:42px;width:590px;height:434px;background:radial-gradient(circle at 50% 45%,#35496b,#1c2a45 70%);border:1px solid #1a263c}

/* loan table */
.loans{left:120px;top:733px;width:960px}
.loans-head{display:flex;height:52px;background:var(--navy);border-top:6px solid #516a90}
.loans-head div{display:flex;align-items:center;justify-content:center;font-size:16px;font-weight:600;border-right:2px solid #2c3b56}
.loans-body{margin-top:8px}
.row{display:flex;height:101px}
.row:nth-child(odd){background:var(--row-a)}
.row:nth-child(even){background:var(--row-b)}
.row>div{border-right:2px solid var(--line);padding:20px 12px;font-size:12px;line-height:19px}
.c1{width:148px}.c2{width:329px}.c3{width:120px}.c4{width:94px}.c5{width:138px}.c6{width:131px;border-right:none!important}
.lender{display:flex;align-items:center;justify-content:center;padding:0!important}
.lender span{width:112px;height:52px;background:#fff;border:3px solid #1a263c;color:#1b2840;font-weight:700;font-size:16px;display:flex;align-items:center;justify-content:center}
.c2 strong{font-size:15px;display:block;line-height:18px}
.c2 b{font-weight:700}
.c2 p{color:var(--muted);font-size:11px;line-height:17px}
.c3,.c4{text-align:center;font-weight:600}
.c5{color:var(--muted);font-size:11px!important;line-height:18px!important}
.c6{display:flex;flex-direction:column;align-items:center;gap:6px;padding-top:14px!important}
.stars{color:var(--star);font-size:15px;letter-spacing:1px}
.stars i{color:#7c8799;font-style:normal}

/* article */
.article{left:120px;top:1243px;width:960px}
.article-head{height:52px;background:var(--navy);border-top:6px solid #516a90;display:flex;align-items:center;justify-content:center;font-size:23px;font-weight:600;letter-spacing:1px}
.article-body{margin-top:12px;height:425px;padding:10px 36px 0 14px}
.post{padding:4px 0 14px;border-bottom:1px dotted #a6b2c6;margin-bottom:14px}
.post:last-child{border-bottom:none}
.post h2{font-size:19px;font-weight:600;margin-bottom:6px}
.post p{font-size:12.5px;line-height:20px;color:var(--text)}
.scrollbar{right:6px;width:8px;border-radius:4px;background:#c9d2df}

/* widgets */
.widgets{left:120px;top:1775px;width:960px;display:flex;gap:16px}
.widget{width:228px;height:429px}
.widget-head{height:48px;background:var(--navy);border-top:6px solid #516a90;display:flex;align-items:center;justify-content:center;text-align:center;font-size:12px;font-weight:600;line-height:16px;text-transform:uppercase}
.widget-body{margin-top:8px;height:373px;padding:16px 12px;font-size:12px;line-height:20px}
.label{font-size:11.5px;font-weight:600;margin-bottom:6px;display:block}
.field{height:28px;background:var(--field);border:1px solid #13203a;margin-bottom:16px}
.btns{display:flex;justify-content:flex-end;gap:6px;margin:-4px 0 14px}
.sm{background:linear-gradient(#d4d7dc,#9da2aa);color:#1b2840;font-size:11px;font-weight:600;padding:2px 7px;border-radius:2px;border:1px solid #5c636f;display:inline-block}
.score{display:flex;align-items:center;gap:10px;font-style:italic;font-weight:700;font-size:15px}
.score .field{flex:1;margin:0}
.radio{display:flex;align-items:center;gap:8px;margin-bottom:16px;font-size:13px}
.radio span{width:14px;height:14px;border-radius:50%;background:#c9cfd8;border:2px solid #8993a3}
.radio span.on{background:radial-gradient(circle,var(--accent) 35%,#fff 40%)}
.budget-art{width:110px;height:110px;margin:22px 0 0 20px;background:radial-gradient(circle,#a6c642,#4d6a29);border-radius:8px}
.help ol{padding-left:16px;margin:8px 0 30px}
.help li{margin-bottom:12px;line-height:16px}

/* footer */
.footer{left:0;top:2246px;width:1200px;height:95px;background:var(--navy);text-align:center}
.footer-name{font-size:29px;font-weight:700;color:#101a2c;margin-top:8px;letter-spacing:1px}
.footer small{display:block;font-size:12px;color:#7d8ba3;margin-top:6px}
</style>
</head>
<body>

<div class="abs socials" aria-label="Social links"><span></span><span></span><span></span><span></span><span></span></div>
<div class="abs brand"><span class="brand-name">PELLROWATT</span></div>
<div class="abs account"><span class="btn-dark">Login</span><span class="btn-dark">Register</span></div>

<nav class="abs nav">
  <a class="active">Home</a><a>All about finances</a><a>Economics dictionary</a><a>About us</a><a>Contact</a><a>Forum</a>
</nav>

<section class="abs hero panel">
  <div class="lip" style="margin-top:-18px"></div>
  <div class="abs hero-copy">
    <h1>Lorem Ipsum Doler</h1>
    <p>Lorem ipsum doler set amount this is dummy text for tempLorem ipsum dolor sit amet, consectetur adipiscing elit.</p>
    <p>Curabitur commodo vehieu pellentesque ante laoreet nec. Pellentesque habitant morbi tristique senectusmalesuada.</p>
    <p>Curabitur commodo vehieu pellentesque ante laoreet nec. Pellentesque habitant morbi tristique senectusmalesuada.Pelle ntesque habitant morbi tristique.</p>
    <span class="btn-light">Read more ▸</span>
  </div>
  <div class="abs hero-art" role="img" aria-label="Illustration of an advisor connected to a network of clients"></div>
</section>

<section class="abs loans">
  <div class="loans-head">
    <div class="c1">Loan</div><div class="c2">Information</div><div class="c3">Amount</div><div class="c4">Period</div><div class="c5">Open for</div><div class="c6"></div>
  </div>
  <div class="loans-body panel">
    <div class="row">
      <div class="c1 lender"><span>Calderbank</span></div>
      <div class="c2"><strong>Tessly</strong><p><b>Consumer loans.</b> Marten Vollby helps small and large loans. Excl. 25.000, 29.33% eff, 25,000 o / 5 years, geb. 785, total 44,878.</p></div>
      <div class="c3">5000-25000</div><div class="c4">1-5 years</div>
      <div class="c5">Filled 20 years.<br>Fixed income.<br>No betalingsanm.</div>
      <div class="c6"><svg width="30" height="30" viewBox="0 0 30 30"><circle cx="15" cy="15" r="14" fill="#3d8fe0"/><circle cx="13" cy="13" r="6" fill="none" stroke="#fff" stroke-width="2.5"/><line x1="17" y1="17" x2="22" y2="22" stroke="#fff" stroke-width="3"/></svg><span class="stars">★★★★<i>★</i></span></div>
    </div>
    <div class="row">
      <div class="c1 lender"><span>Orvenmoney</span></div>
      <div class="c2"><strong>Tessly</strong><p><b>Consumer loans.</b> Marten Vollby helps small and large loans. Excl. 25.000, 29.33% eff, 25,000 o / 5 years, geb. 785, total 44,878.</p></div>
      <div class="c3">5000-25000</div><div class="c4">1-5 years</div>
      <div class="c5">Filled 20 years.<br>Fixed income.<br>No betalingsanm.</div>
      <div class="c6"><svg width="30" height="30" viewBox="0 0 30 30"><circle cx="15" cy="15" r="14" fill="#3d8fe0"/><circle cx="13" cy="13" r="6" fill="none" stroke="#fff" stroke-width="2.5"/><line x1="17" y1="17" x2="22" y2="22" stroke="#fff" stroke-width="3"/></svg><span class="stars">★★★★<i>★</i></span></div>
    </div>
    <div class="row">
      <div class="c1 lender"><span>Tessly</span></div>
      <div class="c2"><strong>Tessly</strong><p><b>Consumer loans.</b> Marten Vollby helps small and large loans. Excl. 25.000, 29.33% eff, 25,000 o / 5 years, geb. 785, total 44,878.</p></div>
      <div class="c3">5000-25000</div><div class="c4">1-5 years</div>
      <div class="c5">Filled 20 years.<br>Fixed income.<br>No betalingsanm.</div>
      <div class="c6"><svg width="30" height="30" viewBox="0 0 30 30"><circle cx="15" cy="15" r="14" fill="#3d8fe0"/><circle cx="13" cy="13" r="6" fill="none" stroke="#fff" stroke-width="2.5"/><line x1="17" y1="17" x2="22" y2="22" stroke="#fff" stroke-width="3"/></svg><span class="stars">★★★★<i>★</i></span></div>
    </div>
    <div class="row">
      <div class="c1 lender"><span>Brindo</span></div>
      <div class="c2"><strong>Tessly</strong><p><b>Consumer loans.</b> Marten Vollby helps small and large loans. Excl. 25.000, 29.33% eff, 25,000 o / 5 years, geb. 785, total 44,878.</p></div>
      <div class="c3">5000-25000</div><div class="c4">1-5 years</div>
      <div class="c5">Filled 20 years.<br>Fixed income.<br>No betalingsanm.</div>
      <div class="c6"><svg width="30" height="30" viewBox="0 0 30 30"><circle cx="15" cy="15" r="14" fill="#3d8fe0"/><circle cx="13" cy="13" r="6" fill="none" stroke="#fff" stroke-width="2.5"/><line x1="17" y1="17" x2="22" y2="22" stroke="#fff" stroke-width="3"/></svg><span class="stars">★★★★<i>★</i></span></div>
    </div>
  </div>
  <div class="abs scrollbar" style="top:78px;height:20px"></div>
</section>

<section class="abs article">
  <div class="article-head">ARTICLE</div>
  <div class="article-body panel">
    <div class="post"><h2>Lorem ipsum dolor sit amet</h2><p>Lorem ipsum dolor sit amet, consectetur adipiscing elit. Morbi id nisl quam, sed consectetur tellus. Suspendisse at justo posuere diam aliquam consectetur. Pellentesque dictum, turpis vel ullamcorper blandit, justo purus venenatis nibh, placerat iaculis turpis nulla quis felis. Vivamus lacus libero, lobortis ut imperdiet feugiat, semper at odio. Quisque volutpat sagittis purus mattis rutrum. Maecenas facilisis ullamcorper augue nec varius. Proin tristique lacinia lobortis.</p></div>
    <div class="post"><h2>Lorem ipsum dolor sit amet</h2><p>Lorem ipsum dolor sit amet, consectetur adipiscing elit. Morbi id nisl quam, sed consectetur tellus. Suspendisse at justo posuere diam aliquam consectetur. Pellentesque dictum, turpis vel ullamcorper blandit, justo purus venenatis nibh, placerat iaculis turpis nulla quis felis. Vivamus lacus libero, lobortis ut imperdiet feugiat, semper at odio. Quisque volutpat sagittis purus mattis rutrum. Maecenas facilisis ullamcorper augue nec varius. Proin tristique lacinia lobortis.</p></div>
    <div class="post"><h2>Lorem ipsum dolor sit amet</h2><p>Lorem ipsum dolor sit amet, consectetur adipiscing elit. Morbi id nisl quam, sed consectetur tellus. Suspendisse at justo posuere diam aliquam consectetur. Pellentesque dictum, turpis vel ullamcorper blandit, justo purus venenatis nibh, placerat iaculis turpis nulla quis felis. Vivamus lacus libero, lobortis ut imperdiet feugiat, semper at odio. Quisque volutpat sagittis purus mattis rutrum. Maecenas facilisis ullamcorper augue nec varius. Proin tristique lacinia lobortis.</p></div>
  </div>
  <div class="abs scrollbar" style="top:76px;height:20px"></div>
</section>

<section class="abs widgets">
  <div class="widget">
    <div class="widget-head">Calculate your<br>monthly performance</div>
    <div class="widget-body panel">
      <span class="label">Your loan amount (fx 10000)</span><div class="field"></div>
      <span class="label">Loan term (in months)</span><div class="field"></div>
      <span class="label">Effective interest rate (use a dot fx 6.3)</span><div class="field"></div>
      <div class="btns"><span class="sm">Calculate</span><span class="sm">Slett</span></div>
      <span class="label">Monthly performance före tax</span>
      <div class="score">Score <div class="field"></div></div>
    </div>
  </div>
  <div class="widget">
    <div class="widget-head">Reconciliation</div>
    <div class="widget-body panel">
      <span class="label">Have you added a private budget?:</span><div class="field" style="margin-bottom:20px"></div>
      <div class="radio"><span class="on"></span>Yes</div>
      <div class="radio"><span></span>No - not endda</div>
      <div class="radio"><span></span>Budget, what is it?</div>
      <span class="sm" style="margin-left:30px">Vote</span>
    </div>
  </div>
  <div class="widget">
    <div class="widget-head">Get laid a budget here</div>
    <div class="widget-body panel">
      <p style="color:var(--muted)">Everyone needs a budget. Get more insight into your finances using our budsjettark. All it requires is Tabulo from Quenview Suite package.</p>
      <span class="sm" style="margin-top:10px">Get budget sheet here</span>
      <div class="budget-art" role="img" aria-label="Illustration of a folder with budget sheets and coins"></div>
    </div>
  </div>
  <div class="widget help">
    <div class="widget-head">Find what you are looking for</div>
    <div class="widget-body panel">
      <strong style="font-size:13px">Get help here. You can either:</strong>
      <ol>
        <li>Search across Nordic Banks and find the answer</li>
        <li>Find your answer in the "Advice" (FAQ)</li>
        <li>Contact us , if a technical fault with the capacity or</li>
      </ol>
      <span class="label">applications Search sity ::</span><div class="field" style="margin-bottom:10px"></div>
      <span class="sm">Find what you are looking for</span>
    </div>
  </div>
</section>

<footer class="abs footer">
  <div class="footer-name">PELLROWATT</div>
  <small>Copyright © Pellrowatt 2013 - All Rights Reserved</small>
</footer>

</body>
</html>
```